Stationery Required - Own Logo provided

Hi,

We are a retail company called 'Copperfinch Trading Limited' based in the UK and would like some corporate stationery designed.

We have provided our Logo which we would like to use (Its attached to this brief)...

The designs must be orginal, professional, stylish and interesting!

Target Market(s)

We will use this stationery to communicate with our wholesale suppliers and employees, so it must have a 'professional' feel about it.

Industry/Entity Type

It Company

Requirements
Must have
• Must be professional, corporate, stylish and not to 'fussy'. we require ... Business card design, a4 letter, compliment slip. All designs must be supplied in a format where the text (address/telephone numbers etc..) can be edited, as we have alot of staff and operate out of several different premises.
Nice to have
• I would like a windows backround picture file supplied as well so we can integrate that onto our computer systems.

```html
<!DOCTYPE html>
<html lang="en">
<head>
<meta charset="utf-8">
<title>Copperfinch Trading Limited – Stationery</title>
<link rel="stylesheet" href="https://fonts.googleapis.com/css2?family=Lato:wght@400;700&display=swap">
<style>
  :root {
    --brand-green: #8cc63f;
    --paper: #ffffff;
    --ink: #3c3c3c;
    --frame: #555555;
    --shadow: rgba(110, 140, 70, 0.45);
  }
  * { box-sizing: border-box; margin: 0; padding: 0; }
  html, body { width: 1200px; height: 1193px; overflow: hidden; background: var(--paper); }
  body { font-family: "Lato", sans-serif; }

  .board {
    position: relative;
    width: 1200px;
    height: 1193px;
    border: 1.5px solid var(--frame);
    background: var(--paper);
    overflow: hidden;
  }

  /* Shared */
  .wordmark {
    font-family: "Lato", sans-serif;
    font-weight: 700;
    color: var(--brand-green);
    white-space: nowrap;
    display: flex;
    align-items: center;
    gap: 5px;
    line-height: 1;
  }
  .wordmark .mark {
    display: inline-block;
    flex: none;
    background: var(--brand-green);
  }
  /* Vertical text reading bottom-to-top, starting at the bottom of its box */
  .vertical {
    position: absolute;
    writing-mode: vertical-rl;
    transform: rotate(180deg);
  }

  /* A4 letter */
  .letter {
    position: absolute;
    left: 331px;
    top: 69px;
    width: 737px;
    height: 1044px;
    filter: drop-shadow(8px 16px 14px var(--shadow));
  }
  .letter svg { position: absolute; inset: 0; }
  .letter .address {
    left: 698px;
    top: 362px;
    height: 282px;
    font-size: 11px;
    font-weight: 700;
    line-height: 1.2;
    color: var(--ink);
    white-space: nowrap;
  }
  .letter .wordmark {
    left: 690px;
    top: 652px;
    height: 198px;
    font-size: 17px;
  }
  .letter .wordmark .mark { width: 15px; height: 15px; }

  /* Compliment slip */
  .slip {
    position: absolute;
    left: 94px;
    top: 573px;
    width: 813px;
    height: 359px;
    background: var(--paper);
    border: 1.5px solid var(--brand-green);
    box-shadow: 8px 16px 16px var(--shadow);
  }
  .slip .wordmark {
    left: 781px;
    top: 190px;
    height: 152px;
    font-size: 13px;
    gap: 4px;
  }
  .slip .wordmark .mark { width: 11px; height: 11px; }

  /* Business cards */
  .card {
    position: absolute;
    width: 317px;
    height: 159px;
    box-shadow: 8px 14px 14px var(--shadow);
  }
  .card .tab {
    position: absolute;
    top: 61px;
    width: 6px;
    height: 28px;
  }
  .card .tab.left { left: 0; }
  .card .tab.right { right: 0; }

  .card-front {
    left: 249px;
    top: 318px;
    background: var(--paper);
    border: 1.5px solid var(--brand-green);
  }
  .card-front .tab { background: var(--brand-green); top: 63px; }
  .card-front .wordmark {
    position: absolute;
    left: 0; right: 0;
    top: 68px;
    justify-content: center;
    font-size: 17px;
  }
  .card-front .wordmark .mark { width: 14px; height: 14px; }
  .card-front .website {
    position: absolute;
    left: 0; right: 0;
    bottom: 4px;
    text-align: center;
    font-size: 8.5px;
    letter-spacing: 2.6px;
    color: var(--brand-green);
  }

  .card-back {
    left: 125px;
    top: 206px;
    background: var(--brand-green);
    color: var(--paper);
  }
  .card-back .tab { background: var(--paper); opacity: 0.85; }
  .card-back .contact,
  .card-back .postal {
    position: absolute;
    top: 59px;
    font-size: 8.2px;
    line-height: 13px;
  }
  .card-back .contact { left: 19px; }
  .card-back .contact .role { font-size: 6.5px; }
  .card-back .postal { right: 16px; text-align: right; }
</style>
</head>
<body>
<main class="board">

  <section class="letter" aria-label="A4 letterhead">
    <svg width="737" height="1044" viewBox="0 0 737 1044">
      <polygon points="0.75,0.75 550,0.75 736,184 736,1043 0.75,1043"
               fill="var(--paper)" stroke="var(--brand-green)" stroke-width="1.5"/>
      <polygon points="550,0.75 550,184 736,184" fill="var(--brand-green)"/>
    </svg>
    <p class="vertical address">17 mill lane road, Ballyholm, County Down BT19 4QX</p>
    <div class="vertical wordmark"><span class="mark"></span>Copperfinch Trading</div>
  </section>

  <section class="slip" aria-label="Compliment slip">
    <div class="vertical wordmark"><span class="mark"></span>Copperfinch Trading</div>
  </section>

  <section class="card card-front" aria-label="Business card front">
    <span class="tab left"></span>
    <span class="tab right"></span>
    <div class="wordmark"><span class="mark"></span>Copperfinch Trading</div>
    <p class="website">WWW.COPPERFINCH.COM</p>
  </section>

  <section class="card card-back" aria-label="Business card back">
    <span class="tab left"></span>
    <span class="tab right"></span>
    <p class="contact">
      Martin Cole, <span class="role">Company Director</span><br>
      781-555-0142<br>
      copperfinch@mailbox.com
    </p>
    <p class="postal">
      17 mill lane road,<br>
      Ballyholm, County Down<br>
      BT19 4QX
    </p>
  </section>

</main>
</body>
</html>
```